One page design needed for a veteran owned brewery

I need a one page web designed for a brewery that is veteran owned. We give back a portion of our proceeds to veteran based nonprofit groups. halvardbrewing.example It is word press based.

Industry/Entity Type

Craft Brewery

Number of Pages Required

1 page

```html
<!DOCTYPE html>
<html lang="en">
<head>
<meta charset="utf-8">
<title>Halvard Brewery – One Page</title>
<link href="https://fonts.googleapis.com/css2?family=Bree+Serif&family=Dancing+Script:wght@600&family=Montserrat:wght@700&family=Arimo:wght@400;700&display=swap" rel="stylesheet">
<style>
:root{
  --green:#5a9a2a;
  --green-bright:#6cb33f;
  --ink:#1b1b1b;
  --paper:#f2f2ee;
  --card:#ecece7;
  --charcoal:#2e2d2c;
  --charcoal-dark:#1f1f1e;
  --muted:#8f8f8a;
  --white:#ffffff;
}
*{margin:0;padding:0;box-sizing:border-box}
html,body{width:1200px;height:1200px;overflow:hidden;background:var(--white)}
body{font-family:"Arimo",Arial,sans-serif;color:var(--ink)}
.page{position:absolute;left:382px;top:21px;width:410px}
.section{position:relative;width:410px;overflow:hidden}
.abs{position:absolute}
.script{font-family:"Dancing Script",cursive;font-weight:600}
.slab{font-family:"Bree Serif",serif}
.nav-font{font-family:"Montserrat",sans-serif;font-weight:700}

/* header */
.site-header{height:46px;background:var(--paper)}
.nav-link{top:20px;font-size:5.2px;letter-spacing:.2px;color:var(--ink)}
.nav-link.is-active{color:var(--green)}
.nav-link.is-active::after{content:"";position:absolute;left:-3px;right:-3px;top:9px;height:1px;background:var(--green)}
.brand{left:176px;top:15px;display:flex;align-items:center;gap:3px}
.brand-dot{width:9px;height:9px;border-radius:50%;background:var(--green)}
.brand-name{font-family:"Bree Serif",serif;font-size:7.5px;color:var(--ink)}
.menu-icon{left:328px;top:20px;width:6px}
.menu-icon span{display:block;height:1px;background:var(--green);margin-bottom:1.2px}
.header-rule{height:2px;background:var(--green-bright)}

/* hero */
.hero{height:175px}
.hero-photo{inset:0;background:radial-gradient(ellipse at 35% 45%,#6d5440 0%,#3e2d24 45%,#1d1714 100%)}
.hero-title{left:224px;top:67px;font-size:9.6px;line-height:11.5px;color:var(--white)}
.hero-text{left:224px;top:97px;width:110px;font-size:5.4px;line-height:7.2px;color:#e6e0da}

/* about */
.about{height:241px;background:var(--paper)}
.about-image{left:94px;top:39px;width:122px;height:156px;background:linear-gradient(90deg,rgba(242,242,238,0) 0%,#c88a2e 20%,#5a3b1f 50%,#b58a3a 80%,rgba(242,242,238,0) 100%);border-radius:6px}
.eyebrow{font-size:8px;color:var(--ink)}
.section-title{font-family:"Bree Serif",serif;font-size:8.6px;color:var(--green);letter-spacing:.3px}
.small-copy{font-size:3.3px;line-height:5.3px;color:#333}
.btn-dark{left:227px;top:172px;width:51px;height:13px;background:var(--ink);outline:1px solid var(--ink);border:1px solid var(--white);color:var(--white);font-size:4px;display:flex;align-items:center;justify-content:center}

/* process */
.process{height:202px;background:radial-gradient(circle at 30% 30%,#3a3937 0%,var(--charcoal) 55%,#262524 100%)}
.process .eyebrow{color:#e8e8e4}
.process .small-copy{color:#b9b9b3}
.btn-green{left:61px;top:103px;width:50px;height:13px;background:var(--green-bright);border:1px solid var(--white);color:var(--white);font-size:4px;display:flex;align-items:center;justify-content:center;z-index:2}
.process-image{left:120px;top:96px;width:96px;height:106px;background:radial-gradient(ellipse at 50% 50%,#f0c04a 0%,#c07c26 40%,#6d4527 72%,rgba(46,45,44,0) 100%)}
.feature{width:50px}
.feature-title{font-family:"Montserrat",sans-serif;font-weight:700;font-size:3.4px;color:var(--green-bright);margin-bottom:1.5px;letter-spacing:.2px}

/* shop */
.shop{height:244px;background:var(--white)}
.center{left:0;right:0;text-align:center}
.product{width:69px;top:50px}
.product-photo{height:118px;background:linear-gradient(180deg,var(--card),#e2e2dc);position:relative}
.product-photo::after{content:"";position:absolute;left:28px;top:14px;width:13px;height:94px;border-radius:5px 5px 3px 3px;background:linear-gradient(180deg,#4b2d16,#7a4a22 40%,#eee 55%,#ddd 85%,#5d381b)}
.price-row{margin-top:2px;height:10px;border:1px solid var(--ink);display:flex;font-size:3.6px;font-weight:700}
.price-row span{flex:1;display:flex;align-items:center;justify-content:center}
.price-row span:first-child{border-right:1px solid var(--ink);flex:.8}
.cart-btn{height:11px;background:var(--ink);color:var(--white);font-size:3.6px;font-weight:700;display:flex;align-items:center;justify-content:center}

/* testimonial */
.testimonial{height:108px;background:var(--paper)}
.arrow{top:50px;width:12px;height:14px;background:var(--green-bright);display:flex;align-items:center;justify-content:center}
.avatar{left:102px;top:32px;width:51px;height:51px;border-radius:50%;background:radial-gradient(circle at 50% 40%,#8a6a55 0%,#4a3a32 60%,#2a2322 100%)}
.quote-name{left:165px;top:36px;font-size:7.5px}
.quote-text{left:165px;top:47px;width:142px}
.dots{left:165px;top:74px;display:flex;gap:1.5px}
.dots span{width:3px;height:3px;border-radius:50%;background:var(--ink)}

/* footer */
.site-footer{height:122px;background:radial-gradient(circle at 40% 30%,#3a3937 0%,var(--charcoal) 60%,#262524 100%)}
.footer-brand{left:62px;top:34px;display:flex;align-items:center;gap:3px}
.footer-brand .brand-name{color:var(--white);font-size:8px}
.footer-brand .brand-dot{background:var(--white)}
.footer-about{left:62px;top:63px;width:78px;color:#c4c4be}
.footer-title{font-family:"Montserrat",sans-serif;font-weight:700;font-size:4px;color:var(--white);top:44px}
.footer-title::after{content:"";display:block;width:12px;height:1px;background:var(--green-bright);margin-top:1.5px}
.footer-list{font-size:3.2px;line-height:5.4px;color:#c4c4be}
.contact-row{display:flex;align-items:center;gap:3px}
.social{left:221px;top:84px;display:flex;gap:3px}
.social span{width:3.5px;height:3.5px;border-radius:50%;background:var(--green-bright)}
.insta{left:278px;top:54px;width:68px;display:grid;grid-template-columns:repeat(3,1fr);gap:1px}
.insta div{height:21.5px}
.copyright-bar{height:14px;background:var(--charcoal-dark);color:#bdbdb7;font-size:3.4px;display:flex;align-items:center;justify-content:center}
</style>
</head>
<body>
<div class="page">

  <header class="section site-header">
    <a class="abs nav-link nav-font is-active" style="left:78px">HOME</a>
    <a class="abs nav-link nav-font" style="left:110px">ABOUT</a>
    <a class="abs nav-link nav-font" style="left:142px">SERVICES</a>
    <div class="abs brand"><span class="brand-dot"></span><span class="brand-name">HALVARD</span></div>
    <a class="abs nav-link nav-font" style="left:238px">NEWS</a>
    <a class="abs nav-link nav-font" style="left:262px">SHOP</a>
    <a class="abs nav-link nav-font" style="left:286px">CONTACT</a>
    <div class="abs menu-icon"><span></span><span></span><span></span></div>
  </header>
  <div class="header-rule"></div>

  <section class="section hero">
    <div class="abs hero-photo" role="img" aria-label="Photo of friends smiling and clinking beer glasses in a pub"></div>
    <h1 class="abs hero-title slab" style="font-weight:400">Good Beer Brings<br>People Together</h1>
    <p class="abs hero-text">We are a veteran owned and operated brewery, our goal is to donate a percentage of our proceeds to veteran organizations and our local heroes.</p>
  </section>

  <section class="section about">
    <div class="abs about-image" role="img" aria-label="Photo of a craft beer bottle beside a full pint glass and a bottle cap"></div>
    <p class="abs eyebrow script" style="left:227px;top:76px">About Craft Beer</p>
    <h2 class="abs section-title" style="left:227px;top:88px">HALVARD BREWERY</h2>
    <div class="abs small-copy" style="left:227px;top:107px;width:100px">
      <p>Halvard Brewery is a craft brewery in Harlow Bay. In that we have a wide breadth of beers with a full kitchen.</p>
      <p style="margin-top:4px">We believe the transition from military life to civilian life can be a difficult road. We are trained by the military to be tough, battle hardened soldiers ready for combat. However, the skill training is not nearly enough to fight the difference of civilian life, leaving some vets feeling left behind and causing many to take their own life.</p>
      <p style="margin-top:4px">The Halvard Brewery will work to change that!</p>
    </div>
    <a class="abs btn-dark">View more</a>
  </section>

  <section class="section process">
    <p class="abs eyebrow script" style="left:61px;top:33px">How We Create Our</p>
    <h2 class="abs section-title" style="left:61px;top:45px">CRAFT BEER</h2>
    <p class="abs small-copy" style="left:61px;top:64px;width:98px">Malorum phaedrum torquatos nec eu, vis detraxit periculis ex, nihil expetendis in mei. Mei an pericula euripidis, hinc partem ei est. Eos ei nisl graecis, vix aperiri consequat an. Eius lorem tincidunt vix at, vel pertinax sensibus id, error epicurei mea et. Mea facilisis urbanitas moderatius id.</p>
    <div class="abs process-image" role="img" aria-label="Photo of a foaming beer mug on a wooden barrel with wheat stalks"></div>
    <a class="abs btn-green">Submit</a>
    <div class="abs feature" style="left:230px;top:52px"><p class="feature-title">QUALITY INGREDIENTS</p><p class="small-copy">Lorem ipsum dolor sit amet, consectetuer adipiscing elit, sed diam nonummy nibh euismod.</p></div>
    <div class="abs feature" style="left:298px;top:52px"><p class="feature-title">NATURAL SUNSHINE</p><p class="small-copy">Lorem ipsum dolor sit amet, consectetuer adipiscing elit, sed diam nonummy.</p></div>
    <div class="abs feature" style="left:230px;top:101px"><p class="feature-title">FERMENTATION</p><p class="small-copy">Lorem ipsum dolor sit amet, consectetuer adipiscing elit, sed diam nonummy.</p></div>
    <div class="abs feature" style="left:298px;top:101px"><p class="feature-title">UNRIVALLED TASTE</p><p class="small-copy">Lorem ipsum dolor sit amet, consectetuer adipiscing elit, sed diam nonummy nibh euismod tincidunt ut laoreet dolore.</p></div>
  </section>

  <section class="section shop">
    <p class="abs center eyebrow script" style="top:18px">Our Shop</p>
    <h2 class="abs center section-title" style="top:30px">CRAFT BEER</h2>
    <div class="abs product" style="left:61px">
      <div class="product-photo" role="img" aria-label="Photo of a brown beer bottle with a green and white label"></div>
      <div class="price-row"><span>$16</span><span>CRAFT BEER</span></div>
      <div class="cart-btn">ADD TO CART</div>
    </div>
    <div class="abs product" style="left:133px">
      <div class="product-photo" role="img" aria-label="Photo of a brown beer bottle with a black and white striped label"></div>
      <div class="price-row"><span>$16</span><span>CRAFT BEER</span></div>
      <div class="cart-btn">ADD TO CART</div>
    </div>
    <div class="abs product" style="left:205px">
      <div class="product-photo" role="img" aria-label="Photo of a brown beer bottle with a blue and white label"></div>
      <div class="price-row"><span>$16</span><span>CRAFT BEER</span></div>
      <div class="cart-btn">ADD TO CART</div>
    </div>
    <div class="abs product" style="left:277px">
      <div class="product-photo" role="img" aria-label="Photo of a brown beer bottle with an orange fruit label"></div>
      <div class="price-row"><span>$16</span><span>CRAFT BEER</span></div>
      <div class="cart-btn">ADD TO CART</div>
    </div>
  </section>

  <section class="section testimonial">
    <div class="abs arrow" style="left:61px"><svg width="5" height="7" viewBox="0 0 5 7"><path d="M4 0.5 L1 3.5 L4 6.5" fill="none" stroke="#fff" stroke-width="0.8"/></svg></div>
    <div class="abs avatar" role="img" aria-label="Portrait photo of a customer at a bar"></div>
    <p class="abs quote-name script">Marisa Dunlow</p>
    <p class="abs quote-text small-copy">Malorum phaedrum torquatos nec eu, vis detraxit periculis ex, nihil expetendis in mei. Mei an pericula euripidis, hinc partem ei est. Eos ei nisl graecis, vix aperiri consequat an. Eius lorem tincidunt vix at, vel pertinax sensibus id, error epicurei mea et. Mea facilisis urbanitas moderatius id. Vis ei rationibus definiebas, eu qui purto zril laoreet.</p>
    <div class="abs dots"><span></span><span></span><span></span></div>
    <div class="abs arrow" style="left:326px"><svg width="5" height="7" viewBox="0 0 5 7"><path d="M1 0.5 L4 3.5 L1 6.5" fill="none" stroke="#fff" stroke-width="0.8"/></svg></div>
  </section>

  <footer class="section site-footer">
    <div class="abs footer-brand"><span class="brand-dot"></span><span class="brand-name">HALVARD</span></div>
    <div class="abs footer-about small-copy">
      <p>We are a veteran owned brewery, brewing for veterans and local heroes.</p>
      <p>Coming to Harlow Bay in 2019.</p>
      <p>Owen Brask, Founder, Owner, Brewer</p>
      <p style="margin-top:3px">Veteran, 1985–1994</p>
    </div>

    <p class="abs footer-title" style="left:155px">WORKING HOURS</p>
    <ul class="abs footer-list" style="left:155px;top:55px;list-style:none">
      <li>Monday</li><li>Tuesday</li><li>Wednesday</li><li>Thursday</li><li>Friday</li><li>Saturday</li><li>Sunday: Closed</li>
    </ul>

    <p class="abs footer-title" style="left:221px">FIND US ON</p>
    <div class="abs footer-list" style="left:221px;top:56px">
      <div class="contact-row"><svg width="4" height="4" viewBox="0 0 4 4"><path d="M2 0.2C1 0.2 0.5 0.9 0.5 1.6 0.5 2.6 2 3.8 2 3.8S3.5 2.6 3.5 1.6C3.5 0.9 3 0.2 2 0.2Z" fill="#fff"/></svg><span>Fennwick Road 12, Harlow Bay</span></div>
      <div class="contact-row"><svg width="4" height="4" viewBox="0 0 4 4"><rect x="0.3" y="0.8" width="3.4" height="2.4" fill="#fff"/><path d="M0.3 0.8 L2 2.2 L3.7 0.8" fill="none" stroke="#333" stroke-width="0.3"/></svg><span>info@halvardbrewing.example</span></div>
      <div class="contact-row"><svg width="4" height="4" viewBox="0 0 4 4"><rect x="1" y="0.2" width="2" height="3.6" rx="0.4" fill="none" stroke="#fff" stroke-width="0.5"/></svg><span>555 010 4400</span></div>
    </div>
    <div class="abs social"><span></span><span></span><span></span><span></span><span></span></div>

    <p class="abs footer-title" style="left:278px">FOLLOW INSTAGRAM</p>
    <div class="abs insta">
      <div role="img" aria-label="Photo of food and beer" style="background:linear-gradient(135deg,#c9893a,#6b3d1c)"></div>
      <div role="img" aria-label="Photo of a plated meal" style="background:linear-gradient(135deg,#e2c9a0,#8a6a48)"></div>
      <div role="img" aria-label="Photo of bottled beers" style="background:linear-gradient(135deg,#6a4a2e,#2d2018)"></div>
      <div role="img" aria-label="Photo of a pub table" style="background:linear-gradient(135deg,#a66b34,#4a2e1a)"></div>
      <div role="img" aria-label="Photo of baked bread" style="background:linear-gradient(135deg,#d6a05a,#87572a)"></div>
      <div role="img" aria-label="Photo of a dish with sauce" style="background:linear-gradient(135deg,#c08a4e,#5e3a20)"></div>
    </div>
  </footer>
  <div class="copyright-bar">Copyright © Halvard Brewery</div>

</div>
</body>
</html>
```